We need a set of stationary to compliment our new logo including letterhead (A4 & A5), envelopes, Business cards and appointment cards.

Hi Designers - our details are set out below.
Ashbrook Family Medical
Shop 7, 23-25 Tolley Parade
GAWLER EAST SA 5118
Phone - 08 84967342
Fax - 08 84967349
www.ashbrookfm-example.com.au

Cheers Meg

Industry/Entity Type

Medical

Requirements
Must have
• Reflect the logo be modern and classy

```html
<!DOCTYPE html>
<html lang="en">
<head>
<meta charset="utf-8">
<title>Ashbrook Family Medical – Business &amp; Appointment Cards</title>
<link rel="stylesheet" href="https://fonts.googleapis.com/css2?family=Lato:ital,wght@0,400;0,700;1,400&family=Raleway:wght@400&display=swap">
<style>
  :root {
    --page-bg: #e9e7e3;
    --brand-blue: #1b8fd2;
    --brand-green: #8dc63f;
    --card-white: #f7f7f5;
    --ink: #333333;
    --rule: #9a9a9a;
    --white: #ffffff;
    --faint-mark: rgba(141, 198, 63, 0.12);
  }
  * { margin: 0; padding: 0; box-sizing: border-box; }
  html, body { width: 1200px; height: 900px; overflow: hidden; }
  body {
    background: var(--page-bg);
    font-family: "Lato", Arial, sans-serif;
    color: var(--ink);
    position: relative;
  }
  .card {
    position: absolute;
    width: 560px;
    height: 320px;
    box-shadow: 0 6px 18px rgba(0,0,0,0.18);
    overflow: hidden;
  }

  /* Front: business card */
  .card-front {
    left: 110px; top: 80px;
    background: var(--brand-blue);
    display: flex; flex-direction: column; align-items: center; justify-content: center;
  }
  .brand-dot {
    width: 70px; height: 70px; border-radius: 50%;
    background: var(--brand-green);
    margin-bottom: 22px;
  }
  .brand-name {
    font-family: "Raleway", Arial, sans-serif;
    font-weight: 400;
    font-size: 30px;
    letter-spacing: 2px;
    color: var(--white);
    text-transform: uppercase;
  }
  .website {
    margin-top: 36px;
    font-size: 15px;
    letter-spacing: 0.5px;
    color: var(--white);
  }

  /* Back: appointment card */
  .card-back {
    left: 530px; top: 490px;
    background: var(--card-white);
  }
  .faint-mark {
    position: absolute; right: -30px; top: 60px;
    width: 230px; height: 230px; border-radius: 50%;
    background: var(--faint-mark);
  }
  .band {
    position: absolute; left: 0; right: 0; top: 22px; height: 30px;
    background: var(--brand-green);
    color: var(--white);
    display: flex; align-items: center; justify-content: space-between;
    padding: 0 170px 0 26px;
    font-size: 14px; letter-spacing: 0.6px;
  }
  .appointments {
    position: absolute; left: 24px; right: 24px; top: 58px;
    display: grid; grid-template-columns: 1fr 1fr; column-gap: 20px;
  }
  .column-right { padding-top: 22px; }
  .slot { margin-bottom: 10px; font-size: 10px; letter-spacing: 0.3px; }
  .field { display: flex; align-items: flex-end; height: 19px; }
  .field .label { width: 38px; }
  .field .line { flex: 1; border-bottom: 1px solid var(--rule); height: 11px; }
  .field .line.short { flex: 0 0 120px; }
  .field .ampm { margin-left: 8px; }
  .notice {
    position: absolute; left: 24px; right: 20px; bottom: 18px;
    font-style: italic; font-size: 11.5px; color: #555;
  }
</style>
</head>
<body>
  <section class="card card-front" aria-label="Business card front">
    <div class="brand-dot"></div>
    <div class="brand-name">Ashbrook Family Medical</div>
    <div class="website">www.ashbrookfm-example.com.au</div>
  </section>

  <section class="card card-back" aria-label="Appointment card">
    <div class="faint-mark"></div>
    <div class="band">
      <span>YOUR APPOINTMENTS:</span>
      <span>T&nbsp;&nbsp;08 84967342</span>
    </div>
    <div class="appointments">
      <div class="column-left">
        <div class="slot">
          <div class="field"><span class="label">DATE</span><span class="line"></span></div>
          <div class="field"><span class="label">TIME</span><span class="line short"></span><span class="ampm">AM | PM</span></div>
        </div>
        <div class="slot">
          <div class="field"><span class="label">DATE</span><span class="line"></span></div>
          <div class="field"><span class="label">TIME</span><span class="line short"></span><span class="ampm">AM | PM</span></div>
        </div>
        <div class="slot">
          <div class="field"><span class="label">DATE</span><span class="line"></span></div>
          <div class="field"><span class="label">TIME</span><span class="line short"></span><span class="ampm">AM | PM</span></div>
        </div>
      </div>
      <div class="column-right">
        <div class="slot">
          <div class="field"><span class="label">DATE</span><span class="line"></span></div>
          <div class="field"><span class="label">TIME</span><span class="line short"></span><span class="ampm">AM | PM</span></div>
        </div>
        <div class="slot">
          <div class="field"><span class="label">DATE</span><span class="line"></span></div>
          <div class="field"><span class="label">TIME</span><span class="line short"></span><span class="ampm">AM | PM</span></div>
        </div>
        <div class="slot">
          <div class="field"><span class="label">DATE</span><span class="line"></span></div>
          <div class="field"><span class="label">TIME</span><span class="line short"></span><span class="ampm">AM | PM</span></div>
        </div>
      </div>
    </div>
    <p class="notice">Please note fees will be charged for missed appointments without 48 hours notice.</p>
  </section>
</body>
</html>
```